Surgical Sales Presentation Folder

Presentation folder; three panel; custom cutouts; Six 8.5 x 11 full color sales sheets to be bound into presentation folder; 5 full color sales sheets, stepped, longest being 8.5 x 11.
We are Brantley Surgical Group and we are a surgical company that supports physicians who wish to become surgeons. Our clients are Physicians. As such, the design needs to be very professional.
I have included a list of photos and a letter describing what we like about each photo. I have included the verbiage with page identifiers. If this makes scene, please feel free to add photos to the inside of the folder or I can provide you with examples that we think are similar to what we are looking for.
Updates
Target Market(s)
Doctors who want to be surgeons.
Industry/Entity Type
Sales
Requirements
Must have
- Presentation folder; three panel; custom cutouts; Six 8.5 x 11 full color sales sheets to be bound into presentation folder; 5 full color sales sheets, stepped, longest being 8.5 x 11.

```html
<!DOCTYPE html>
<html lang="en">
<head>
<meta charset="utf-8">
<title>Brantley Surgical Group – Presentation Folder Layout</title>
<link href="https://fonts.googleapis.com/css2?family=Russo+One&family=Montserrat:wght@400;600;700&display=swap" rel="stylesheet">
<style>
  :root{
    --brand-blue:#29aae1;
    --brand-navy:#1f4f86;
    --paper:#ffffff;
    --score-pink:#e58fc4;
    --die-grey:#e2e2e2;
    --label-ink:#2b2b2b;
    --photo-tone-a:#c9a88e;
    --photo-tone-b:#5a4a44;
  }
  html,body{margin:0;padding:0;overflow:hidden;}
  body{width:828px;height:1200px;background:var(--paper);position:relative;}
  .folder-layout{position:absolute;inset:0;width:828px;height:1200px;display:block;}
  .view-label{font-family:"Russo One",sans-serif;font-size:39px;fill:var(--label-ink);text-anchor:middle;}
  .brand-name{font-family:"Montserrat",sans-serif;font-weight:700;font-size:8.5px;fill:var(--brand-navy);letter-spacing:.2px;}
  .bio-text,.body-copy{font-family:"Montserrat",sans-serif;font-weight:400;font-size:3.8px;fill:var(--paper);}
  .section-heading{font-family:"Montserrat",sans-serif;font-weight:700;font-size:4.4px;fill:var(--paper);}
  .blue-fill{fill:var(--brand-blue);}
  .paper-fill{fill:var(--paper);}
  .score-line{stroke:var(--score-pink);stroke-width:1;fill:none;}
  .die-outline{stroke:var(--die-grey);stroke-width:1;fill:var(--paper);}
</style>
</head>
<body>
<svg class="folder-layout" viewBox="0 0 828 1200" xmlns="http://www.w3.org/2000/svg">
  <defs>
    <radialGradient id="portrait-tone" cx="50%" cy="45%" r="60%">
      <stop offset="0%" stop-color="var(--photo-tone-a)"/>
      <stop offset="100%" stop-color="var(--photo-tone-b)"/>
    </radialGradient>
  </defs>

  <!-- FRONT VIEW -->
  <text class="view-label" x="447" y="123">FRONT</text>
  <g class="front-cover">
    <rect class="blue-fill" x="354" y="140" width="183" height="244"/>
    <path class="paper-fill" d="M354,140 H398 C460,150 492,210 490,262 C488,320 455,372 405,384 H354 Z"/>
    <line class="score-line" x1="474" y1="222" x2="474" y2="306"/>
    <line class="score-line" x1="477" y1="222" x2="477" y2="306"/>
    <g class="handle-cutout">
      <rect class="paper-fill" x="479" y="212" width="40" height="106" rx="18"/>
      <ellipse class="paper-fill" cx="497" cy="262" rx="22" ry="40"/>
    </g>
    <g class="brand-lockup">
      <circle cx="382" cy="260" r="4.2" fill="var(--brand-navy)"/>
      <text class="brand-name" x="389" y="263">Brantley Surgical Group</text>
    </g>
  </g>

  <!-- INSIDE VIEW -->
  <text class="view-label" x="447" y="426">INSIDE</text>
  <g class="inside-spread">
    <path class="die-outline" d="M258,446 H190 C140,446 122,490 120,520 H106 Q98,520 98,530 V600 Q98,612 106,612 H120 C122,640 140,690 190,690 H258"/>

    <g class="panel-left">
      <rect class="blue-fill" x="258" y="446" width="189" height="244"/>
      <rect class="paper-fill" x="258" y="518" width="36" height="37"/>
      <rect class="paper-fill" x="408" y="518" width="39" height="37"/>
      <circle cx="318" cy="486" r="15" fill="var(--paper)"/>
      <circle cx="318" cy="486" r="13" fill="url(#portrait-tone)" role="img" aria-label="Portrait photo of the group's founding surgeon"/>
      <text class="bio-text" x="338" y="482">Dr. Avery Lane, Founder</text>
      <text class="bio-text" x="338" y="487.5">Helping physicians grow</text>
      <text class="bio-text" x="338" y="493">into confident surgeons</text>
      <text class="bio-text" x="338" y="498.5">through training.</text>

      <text class="section-heading" x="300" y="514">ABOUT OUR PROGRAM</text>
      <text class="body-copy" x="300" y="521">Our team guides each</text>
      <text class="body-copy" x="300" y="526">physician through every</text>
      <text class="body-copy" x="300" y="531">step of surgical</text>
      <text class="body-copy" x="300" y="536">practice with care.</text>
      <text class="body-copy" x="300" y="544">We offer hands-on</text>
      <text class="body-copy" x="300" y="549">mentoring and support.</text>

      <text class="body-copy" x="356" y="521">Training sessions are</text>
      <text class="body-copy" x="356" y="526">led by experienced</text>
      <text class="body-copy" x="356" y="531">surgeons who share</text>
      <text class="body-copy" x="356" y="536">proven methods and</text>
      <text class="body-copy" x="356" y="541">real clinical insight.</text>
      <text class="body-copy" x="356" y="549">Join us today.</text>
    </g>

    <g class="panel-center">
      <rect class="paper-fill" x="447" y="446" width="191" height="244" stroke="var(--die-grey)" stroke-width="1"/>
      <line class="score-line" x1="500" y1="532" x2="500" y2="603"/>
      <line class="score-line" x1="516" y1="532" x2="516" y2="603"/>
    </g>

    <g class="panel-right">
      <path class="score-line" d="M640,446 L644,432 H732 L740,446"/>
      <path class="score-line" d="M640,690 L644,704 H732 L740,690"/>
      <path class="blue-fill" d="M638,446 H745 Q765,446 765,466 V670 Q765,690 745,690 H638 Z"/>
    </g>

    <line class="score-line" x1="258" y1="446" x2="258" y2="690"/>
    <line class="score-line" x1="447" y1="446" x2="447" y2="690"/>
    <line class="score-line" x1="638" y1="446" x2="638" y2="690"/>
  </g>

  <!-- BACK VIEW -->
  <text class="view-label" x="447" y="796">BACK</text>
  <rect class="blue-fill back-cover" x="370" y="815" width="185" height="247"/>
</svg>
</body>
</html>
```